Tatami Hall Sport promotional leaflet to attract new members

We are looking to produce a leaflet for a local judo club to attract seniors and juniors 5+ the leaflet needs to encourage people to attend classes and train in the martial art

Tatami Hall Sport are proud members of the KSB UK (mats for every) and practice traditional judo which mean we wear white Gi's to show cleanliness and tradition.

www.tatamihallsport.co.uk

Target Market(s)

Kids from 5+ and Adults

Font styles to use
Serif

Requirements
Must have
• Must include times of training and how to book onto a beginners induction
• it must look enticing and show that Judo is fun for all
• must highlight we open on Tuesdays and Thursdays
• Juniors are from 6.15pm to 7.15pm
• seniors 7.30pm to 9pm
• classes are held at Vantrel Gym, Unit 7, Marlow Row, Denholm Close, Rustington, West Sussex, BN17 8QT
• We practice on a Sprung floor Mat area and is great for men and women
• first two classes free
Nice to have
• Classes are run by an expeirnced team including
• Dan Merrow 5th Dan and international referee
• Luke Merrow 2nd Dan current Global Grappling Union European Champion

```html
<!DOCTYPE html>
<html lang="en">
<head>
<meta charset="utf-8">
<title>Tatami Hall Sport – Leaflet</title>
<link rel="stylesheet" href="https://fonts.googleapis.com/css2?family=Gilda+Display&display=swap">
<style>
  :root {
    --club-red: #b31e27;
    --paper: #e9e5e5;
    --ink: #111111;
    --white-text: #f4ecec;
    --teal: #27d3c0;
    --teal-ring: #66bfb1;
    --teal-ring-bright: #1fd6c8;
    --glow: #0b2b2b;
  }
  html, body { margin: 0; padding: 0; overflow: hidden; }
  body { width: 927px; height: 1200px; background: #ffffff; }
  .leaflet {
    position: relative;
    width: 927px;
    height: 1200px;
    overflow: hidden;
    font-family: "Gilda Display", "Libre Baskerville", serif;
    color: var(--white-text);
  }
  .backdrop { position: absolute; inset: 0; }
  .brand {
    position: absolute;
    left: 624px;
    top: 80px;
    display: flex;
    align-items: center;
    gap: 10px;
  }
  .brand-dot {
    width: 41px; height: 41px;
    border-radius: 50%;
    background: var(--club-red);
  }
  .brand-name {
    font-size: 27px;
    color: var(--ink);
    white-space: nowrap;
    letter-spacing: 0.5px;
  }
  .text { position: absolute; white-space: nowrap; margin: 0; font-weight: 400; }
  .headline-days {
    left: 10px; top: 578px;
    font-size: 28px;
    color: var(--teal);
    letter-spacing: 0.4px;
    text-shadow: 0 0 8px var(--glow), 0 0 14px var(--glow);
  }
  .session { left: 12px; font-size: 24.5px; letter-spacing: 0.5px; }
  .session-juniors { top: 626px; }
  .session-seniors { left: 10px; top: 660px; }
  .booking { left: 12px; top: 712px; font-size: 18px; line-height: 24px; letter-spacing: 0.4px; }
  .booking span { display: block; }
  .venue { left: 420px; font-size: 24px; letter-spacing: 0.6px; line-height: 33px; top: 754px; }
  .venue span { display: block; }
  .floor { left: 421px; top: 860px; font-size: 24px; line-height: 33px; letter-spacing: 0.6px; }
  .floor span { display: block; }
  .offer { left: 486px; top: 946px; font-size: 27.5px; color: var(--teal); letter-spacing: 0.6px; }
  .team { left: 419px; top: 997px; font-size: 21px; letter-spacing: 0.5px; }
  .team span { display: block; height: 37.5px; }
</style>
</head>
<body>
<main class="leaflet">
  <svg class="backdrop" width="927" height="1200" viewBox="0 0 927 1200" xmlns="http://www.w3.org/2000/svg">
    <defs>
      <linearGradient id="dojoTones" x1="0" y1="0" x2="0" y2="1">
        <stop offset="0" stop-color="#3b464c"/>
        <stop offset="0.55" stop-color="#56626a"/>
        <stop offset="1" stop-color="#aab5ae"/>
      </linearGradient>
      <linearGradient id="coachTones" x1="0" y1="0" x2="0.4" y2="1">
        <stop offset="0" stop-color="#3c474d"/>
        <stop offset="0.5" stop-color="#bcc3be"/>
        <stop offset="0.8" stop-color="#c9cdc8"/>
        <stop offset="1" stop-color="#d8514a"/>
      </linearGradient>
      <linearGradient id="groupTones" x1="0" y1="0" x2="0" y2="1">
        <stop offset="0" stop-color="#3e474e"/>
        <stop offset="0.45" stop-color="#4c565d"/>
        <stop offset="0.65" stop-color="#e1e2de"/>
        <stop offset="0.88" stop-color="#d4d7d2"/>
        <stop offset="1" stop-color="#c94a46"/>
      </linearGradient>
    </defs>
    <rect class="paper-field" width="927" height="1200" fill="var(--paper)"/>
    <polygon class="black-wedge" points="623,634 927,362 927,804" fill="var(--ink)"/>
    <polygon class="red-field" points="0,299 927,818 927,1200 434,1200 0,950" fill="var(--club-red)"/>
    <polygon class="white-corner" points="0,950 434,1200 0,1200" fill="#ffffff"/>
    <polygon class="hero-photo" points="0,0 700,0 264,421 0,286" fill="url(#dojoTones)"
             role="img" aria-label="Photo of a judoka performing a throw while club members in white gis watch"/>
    <circle class="coach-photo" cx="691" cy="379" r="208" fill="url(#coachTones)" stroke="var(--teal-ring)" stroke-width="5"
            role="img" aria-label="Photo of a smiling black belt coach standing with two junior judoka in white gis"/>
    <circle class="group-photo" cx="202" cy="983" r="198" fill="url(#groupTones)" stroke="var(--teal-ring-bright)" stroke-width="5"
            role="img" aria-label="Group photo of smiling club members of all ages in white gis on the mat"/>
  </svg>

  <div class="brand">
    <span class="brand-dot"></span>
    <span class="brand-name">Tatami Hall Sport</span>
  </div>

  <h1 class="text headline-days">We open on Tuesdays and Thursdays</h1>
  <p class="text session session-juniors">Juniors are from 6:15pm to 7:15pm</p>
  <p class="text session session-seniors">Seniors are from 7:30pm to 9:00pm</p>

  <p class="text booking">
    <span>Book your beginners induction online at</span>
    <span>www.tatamihallsport.co.uk</span>
  </p>

  <p class="text venue">
    <span>Classes are held at Vantrel Gym,</span>
    <span>Unit 7, Marlow Row, Denholm Close,</span>
    <span>Rustington, West Sussex, BN17 8QT</span>
  </p>
  <p class="text floor">
    <span>We practice on a Sprung floor Mat area</span>
    <span>and is great for men and women</span>
  </p>

  <h2 class="text offer">First two classes free</h2>

  <p class="text team">
    <span>Classes are run by an expeirnced team including</span>
    <span>Dan Merrow 5th Dan and international referee</span>
    <span>Luke Merrow 2nd Dan current Global Grappling</span>
    <span>Union European Champion</span>
  </p>
</main>
</body>
</html>
```